Website design for respected, long standing real estate development company in Central Oregon

Uncoded PSD design only. Homepage and one interior sample page.

Updated website design needed for Halvard Holdings, one of Central Oregon’s oldest and most respected real estate development companies. They develop communities that focus on natural beauty and upscale amenities.

They need a website that features their long, unique history and their current efforts to build smart, healthy and livable communities. They need to tell their story to those who aren't familiar with the company. They need to build credibility and set themselves apart from other real estate development companies.

Current site: http://halvard-holdings.example/

Target Market(s)

Target market is people who are new or plan to relocate to Central Oregon and are researching communities they want to live in.
Secondary markets are potential project partners, and the media. They need to build credibility with these audiences.
The site also needs to be easy to use for non-profits seeking contributions.

Industry/Entity Type

Real Estate Development

Number of Pages Required

Font styles to use
Sans Serif

Requirements
Must have
• Must have simple, user-friendly navigation with organized content.
• Design must be fresh, light and modern.
• Design must use great, high impact imagery that promotes the Central Oregon lifestyle.
• Design must highlight current and future communities and encourage click-throughs to those specific websites.
• Include video element.
• Include social links.
• Do not use dummy copy/lorum ipsum. Use copy from the current site instead. Use correct phone number, address, etc.
Should not have
• Lorum ipsum/dummy copy

```html
<!DOCTYPE html>
<html lang="en">
<head>
<meta charset="utf-8">
<title>Halvard Holdings</title>
<link href="https://fonts.googleapis.com/css2?family=Open+Sans:wght@400;600;700&display=swap" rel="stylesheet">
<style>
:root{
  --plum:#4f2b3d;
  --plum-dark:#3a1f2d;
  --accent:#7b4b7e;
  --text:#555;
  --heading:#333;
  --footer:#2c2c2c;
  --footer-bottom:#222;
  --footer-text:#aaa;
  --white:#fff;
}
*{box-sizing:border-box;margin:0;padding:0}
html,body{width:763px;height:1200px;overflow:hidden}
body{font-family:"Open Sans",Arial,sans-serif;color:var(--text);background:var(--white);position:relative}
.hero{position:absolute;left:0;top:0;width:763px;height:385px;
  background:linear-gradient(180deg,#3a2a48 0%,#5e3f5f 28%,#8a5e70 48%,#6b5560 62%,#3d3a3e 80%,#2b2e2c 100%)}
.hero-scene{position:absolute;inset:0}
.brand{position:absolute;top:14px;left:0;width:763px;display:flex;justify-content:center;align-items:center;gap:8px}
.brand-square{width:22px;height:22px;background:var(--white)}
.brand-name{font-size:12px;font-weight:600;color:var(--white)}
.main-nav{position:absolute;top:62px;left:96px;width:571px;height:22px;background:rgba(58,31,45,.92);display:flex;justify-content:space-between;padding:0 10px;align-items:center}
.main-nav a{font-size:8.5px;color:var(--white);text-decoration:none}
.hero-title{position:absolute;top:165px;width:763px;text-align:center;color:var(--white);font-size:34px;font-weight:400}
.hero-sub{position:absolute;top:213px;width:763px;text-align:center;color:var(--white);font-size:15px}
.arrow{position:absolute;top:204px;width:14px;height:22px}
.arrow.left{left:18px}.arrow.right{right:18px}
.welcome{position:absolute;top:385px;left:0;width:763px;height:190px;text-align:center}
.welcome h1{margin-top:30px;font-size:20px;font-weight:400;color:var(--heading);letter-spacing:.5px}
.welcome p{width:560px;margin:8px auto 0;font-size:7.5px;line-height:1.6}
.btn{display:inline-block;background:var(--plum);color:var(--white);font-size:7.5px;padding:4px 14px;text-decoration:none}
.welcome .btn{margin-top:12px}
.cards{position:absolute;top:590px;left:95px;width:573px;display:flex;justify-content:space-between}
.card{width:178px;text-align:center}
.card-img{height:100px;width:100%}
.card h2{font-size:15px;font-weight:400;color:var(--heading);margin-top:12px}
.card p{font-size:7px;line-height:1.55;margin:5px 8px 7px;height:22px}
.featured{position:absolute;top:805px;left:0;width:763px;height:190px;background:linear-gradient(180deg,#f3f1f2,#e4e0e2)}
.featured h2{text-align:center;font-size:18px;font-weight:400;color:var(--accent);margin-top:16px}
.property{position:absolute;top:50px;display:flex;gap:14px;width:290px}
.property .circle{width:90px;height:90px;border-radius:50%;border:3px solid var(--white);flex:none}
.property h3{font-size:11px;font-weight:700;color:var(--heading);margin-top:10px;text-transform:uppercase}
.property p{font-size:7px;line-height:1.55;margin-top:6px}
.site-footer{position:absolute;top:995px;left:0;width:763px;height:175px;background:var(--footer)}
.footer-brand{position:absolute;left:100px;top:46px;width:42px;height:42px;background:#555}
.footer-col{position:absolute;top:24px}
.footer-col h4{font-size:8.5px;color:var(--white);font-weight:600;margin-bottom:8px;text-transform:uppercase}
.footer-col a,.footer-col span{display:block;font-size:7px;color:var(--footer-text);text-decoration:none;line-height:1.7}
.social{display:flex;gap:5px;margin-top:6px}
.social i{width:12px;height:12px;border-radius:50%;background:#888;display:block}
.copyright{position:absolute;top:1170px;left:0;width:763px;height:30px;background:var(--footer-bottom);font-size:6px;color:#888;text-align:center;line-height:30px}
</style>
</head>
<body>
<header class="hero">
  <div class="hero-scene" role="img" aria-label="Snow-capped mountain above a pine forest at dusk"></div>
  <div class="brand"><span class="brand-square"></span><span class="brand-name">Halvard Holdings</span></div>
  <nav class="main-nav">
    <a href="#">Real Estate Developments</a><a href="#">Real Estate Sales</a><a href="#">Vacation Rentals</a><a href="#">Property Owner Resources</a><a href="#">About Us</a><a href="#">Blog</a>
  </nav>
  <div class="hero-title">Real Estate Developments</div>
  <div class="hero-sub">Livable communities in Central Oregon</div>
  <svg class="arrow left" viewBox="0 0 14 22"><polyline points="11,2 3,11 11,20" fill="none" stroke="#fff" stroke-width="2.5"/></svg>
  <svg class="arrow right" viewBox="0 0 14 22"><polyline points="3,2 11,11 3,20" fill="none" stroke="#fff" stroke-width="2.5"/></svg>
</header>

<section class="welcome">
  <h1>WELCOME TO HALVARD HOLDINGS</h1>
  <p>Halvard Holdings has shaped Central Oregon for more than five decades, creating communities where natural beauty, open space and upscale amenities come together. Our work began with a simple belief: that the land should guide how people live on it, and that every neighborhood should feel rooted in place.</p>
  <p>Today we continue that tradition by building smart, healthy and livable communities for families, retirees and newcomers who are discovering the high desert, the rivers and the mountains that make this region one of the most loved places in the Pacific Northwest.</p>
  <a class="btn" href="#">Read More</a>
</section>

<section class="cards">
  <article class="card">
    <div class="card-img" role="img" aria-label="Handshake over a signed contract" style="background:linear-gradient(135deg,#d9d4cf,#8f8a85)"></div>
    <h2>Real Estate Sales</h2>
    <p>Browse homes and homesites for sale across our communities and river views.</p>
    <a class="btn" href="#">Read More</a>
  </article>
  <article class="card">
    <div class="card-img" role="img" aria-label="Chairlift on a sunny mountain slope" style="background:linear-gradient(180deg,#8fb6d8,#6f8a5a)"></div>
    <h2>Vacation Rental</h2>
    <p>Plan a getaway in a mountain home with trails, golf and the river nearby.</p>
    <a class="btn" href="#">Read More</a>
  </article>
  <article class="card">
    <div class="card-img" role="img" aria-label="Canyon and river landscape with mountains" style="background:linear-gradient(180deg,#7fa9d0,#a07a4e 60%,#5f6e3c)"></div>
    <h2>Our History</h2>
    <p>For over fifty years our builders have helped shape the towns of Central Oregon.</p>
    <a class="btn" href="#">Read More</a>
  </article>
</section>

<section class="featured">
  <h2>Featured Property</h2>
  <div class="property" style="left:100px">
    <div class="circle" role="img" aria-label="Neighborhood park with trees and lawn" style="background:linear-gradient(180deg,#9cc3e0,#5f8a45)"></div>
    <div><h3>Ridgeline Park</h3><p>Our premier west side neighborhood offers trail access, parks and custom homes set among the pines.</p></div>
  </div>
  <div class="property" style="left:390px">
    <div class="circle" role="img" aria-label="Riverfront buildings with autumn trees" style="background:linear-gradient(180deg,#b9c8d6,#b0553a 55%,#6a4b3a)"></div>
    <div><h3>Cedar Riverfront</h3><p>A walkable riverfront community with shops, dining and homes steps from the water's edge and trails.</p></div>
  </div>
</section>

<footer class="site-footer">
  <div class="footer-brand"></div>
  <div class="footer-col" style="left:225px"><h4>Company</h4><a href="#">Home</a><a href="#">About Us</a><a href="#">Blog</a><a href="#">Team</a></div>
  <div class="footer-col" style="left:320px"><h4>Resources</h4><a href="#">Real Estate Developments</a><a href="#">Real Estate Sales</a><a href="#">Vacation Rentals</a><a href="#">Property Owner Resources</a></div>
  <div class="footer-col" style="left:450px"><h4>Support</h4><a href="#">Support</a><a href="#">Terms of Use</a><a href="#">Contact Us</a></div>
  <div class="footer-col" style="left:545px"><h4>Contact Info</h4><span>1000 River Bend Drive, Suite 200</span><span>Bend, OR 97702</span><span>(541) 555-0142</span><span>info@halvard-holdings.example</span>
    <div class="social"><i></i><i></i><i></i><i></i></div></div>
</footer>
<div class="copyright">© 2024 Halvard Holdings. All Rights Reserved.</div>
</body>
</html>
```